Homes, Invest in Non-performing loans

We need only 3 web pages, one for the home, one for the content, one for the properties.
The main focus of our business is to offer non performing loans (before foreclosures) to the general public. All the non-performing mortgages will end in a house, an apartment, a store, etc.
Our customers are able to invest from 10,000usd to 1,000,000usd (average 50,000usd).
Our customers' usual focus groups are employees who want second earnings, perceiving the business feeling without outlay time. They look for a solid finance sense corporation that confers them certainty.
Nearly all our clients desire the house, apartment, store, etc. more than the actual earnings.
The name of our company is BRAMLEY
Reason: We value the time and effort you already invest in our project. We realize that we did't come back on some of the doubts requested by the designers. It will be inequitable to the designers who prerequisite our feedback. We also appreciate the comprehension of the community in this postponement.
Reason: Designers,
We really apreciate all the time and effort you put on our project. From the begining we ask for 3 pages, so now we will leave the 10 finalist and provide some extra time to submit the other 2 pages.
We will race the price in 10%
Target Market(s)
Our customers average investors works as employees and want to have a second income or business without spending time. (People from 35 to 50)
Industry/Entity Type
Finance
Requirements
Should not have
- FLASH

```html
<!DOCTYPE html>
<html lang="en">
<head>
<meta charset="utf-8">
<title>Bramley – Home</title>
<link href="https://fonts.googleapis.com/css2?family=Oswald:wght@500&family=PT+Sans:wght@400;700&family=Tinos&display=swap" rel="stylesheet">
<style>
:root{
  --blue:#2a4fa6;
  --blue-dark:#213f8c;
  --blue-soft:#b7c9e4;
  --field:#aec2e2;
  --btn:#4a9fe0;
  --btn-light:#6bb7ee;
  --page:#e8edf4;
  --white:#ffffff;
  --ink:#1c1c1c;
  --link:#5fa8ff;
}
*{box-sizing:border-box;margin:0;padding:0}
html,body{width:962px;height:1200px;overflow:hidden}
body{position:relative;background:var(--page);font-family:"PT Sans",sans-serif;color:var(--ink)}
.abs{position:absolute}
.header{left:0;top:0;width:962px;height:128px;background:linear-gradient(180deg,#3158b0,var(--blue))}
.brand{left:146px;top:10px;width:113px;height:112px;background:var(--white);border-radius:6px;display:flex;align-items:center;justify-content:center;gap:6px;font-family:"PT Sans",sans-serif;font-weight:700;font-size:19px;color:var(--blue-dark)}
.brand i{width:10px;height:10px;background:var(--blue-dark);display:block}
.login-title{left:656px;top:18px;color:var(--white);font-size:15px}
.field-in{background:var(--white);border-radius:3px;font-size:11px;color:#888;padding:6px 5px}
.btn{background:linear-gradient(180deg,var(--btn-light),var(--btn));color:var(--white);border-radius:10px;text-align:center;font-family:"Tinos",serif}
.forgot{left:660px;top:104px;font-size:11px;color:var(--link)}
.nav{left:0;top:128px;width:962px;height:49px;background:var(--white);font-family:"Tinos",serif;font-size:16px}
.nav span{position:absolute;top:15px}
.nav .sep{width:1px;height:20px;background:#bbb;top:15px}
.search{left:656px;top:13px;width:147px;height:23px;background:#dfe8f5;font-size:13px;padding:4px 27px}
.hero{left:0;top:177px;width:962px;height:465px;background:linear-gradient(180deg,#6f96c9 0%,#a7b8cc 35%,#d8d2b9 60%,#3f6a3a 85%,#577d45 100%)}
.hero-panel{left:118px;top:183px;width:191px;height:340px;background:rgba(110,110,120,.35)}
.hero-text{left:134px;top:280px;color:var(--white);font-family:"Oswald",sans-serif;font-size:17.5px;line-height:25.3px}
.content{left:70px;top:548px;width:811px;height:424px;background:var(--white);border-radius:26px 26px 0 0}
.curve{left:0;top:500px}
.dots{left:408px;top:518px;display:flex;gap:4px}
.dots b{width:11px;height:11px;border-radius:50%;background:#dbe5f2;display:block}
.dots u{width:24px;height:13px;background:#dbe5f2;display:block;margin:0 8px}
.card{top:564px;width:175px;height:200px;background:var(--white);border-radius:14px;box-shadow:0 0 6px rgba(80,100,140,.18);text-align:center}
.card h3{font-weight:400;font-size:14.5px;margin-top:13px}
.card .pic{width:134px;height:69px;margin:6px auto 0}
.card p{text-align:left;font-size:11.2px;line-height:14.5px;padding:6px 0 0 19px}
.card .more{position:absolute;right:26px;bottom:11px;width:48px;height:17px;font-size:9px;line-height:17px;border-radius:3px}
.start{left:657px;top:477px;width:207px;height:298px;background:#f3f6fa}
.start-head{left:657px;top:477px;width:207px;height:58px;background:var(--blue);border-radius:22px 22px 0 0;color:var(--white);font-size:15px;text-align:center;padding-top:24px}
.lbl{left:678px;font-family:"Tinos",serif;font-size:13px}
.inp{left:676px;width:160px;height:25px;background:var(--field)}
.featured{left:114px;top:793px;width:735px;height:179px;background:var(--blue-soft);border-radius:12px}
.featured h2{position:absolute;left:13px;top:8px;font-weight:400;font-size:15px}
.prop{top:28px;height:128px}
.arrow{width:23px;height:14px;background:var(--blue-dark)}
.footer{left:0;top:972px;width:962px;height:228px;background:var(--blue)}
.rule{background:rgba(255,255,255,.5)}
.ft{color:var(--white)}
</style>
</head>
<body>

<header class="abs header">
  <div class="abs brand"><i></i>BRAMLEY</div>
  <div class="abs login-title">Login</div>
  <div class="abs field-in" style="left:654px;top:42px;width:140px;height:23px">username</div>
  <div class="abs field-in" style="left:654px;top:76px;width:140px;height:23px">password</div>
  <div class="abs btn" style="left:803px;top:74px;width:66px;height:27px;line-height:27px;font-family:'PT Sans',sans-serif;font-size:12px;border-radius:4px">Enter</div>
  <div class="abs forgot">Forget Password?</div>
</header>

<nav class="abs nav">
  <svg class="abs" style="left:111px;top:14px" width="16" height="16" viewBox="0 0 16 16"><path d="M1 8 8 1l7 7h-2v7H9v-4H7v4H3V8z" fill="var(--btn)"/></svg>
  <span style="left:130px;color:var(--blue)">Home</span>
  <i class="abs sep" style="left:189px"></i>
  <span style="left:202px">About us</span>
  <i class="abs sep" style="left:272px"></i>
  <span style="left:280px">Nonperforming Loans</span>
  <i class="abs sep" style="left:442px"></i>
  <span style="left:454px">Our Services</span>
  <i class="abs sep" style="left:556px"></i>
  <span style="left:568px">Contact us</span>
  <div class="abs search" style="top:13px;font-size:13px">Search the site</div>
  <svg class="abs" style="left:810px;top:11px" width="27" height="27" viewBox="0 0 27 27"><circle cx="13.5" cy="13.5" r="13.5" fill="var(--blue)"/><circle cx="14.5" cy="12.5" r="3.5" fill="none" stroke="#fff" stroke-width="2"/><path d="M12 15l-3 3" stroke="#fff" stroke-width="2"/></svg>
</nav>

<div class="abs hero" role="img" aria-label="Photo of a two-storey suburban family house with lawn and trees"></div>
<div class="abs hero-panel"></div>
<div class="abs hero-text">HELLO.<br><br>WE SET NEW STANDARDS<br>IN MORTGAGES &amp; HOME<br>LOANS THAT MAKE YOUR<br>FINANCIAL FUTURE HAPPEN<br>... RIGHT NOW</div>
<div class="abs btn" style="left:160px;top:456px;width:89px;height:25px;line-height:25px;font-size:13px;border-radius:13px;box-shadow:0 0 0 3px rgba(255,255,255,.6)">More Info</div>

<svg class="abs curve" width="962" height="60" viewBox="0 0 962 60"><path d="M70 60 Q90 46 200 40 Q380 4 540 4 Q620 4 657 6 L657 60Z" fill="#fff"/></svg>
<div class="abs dots"><u></u><b></b><b></b><b></b><b></b><b></b><u></u></div>

<div class="abs content"></div>

<article class="abs card" style="left:97px">
  <h3>HOME INVESTMENT</h3>
  <div class="pic" role="img" aria-label="Small house model on stacks of banknotes" style="background:linear-gradient(180deg,#cfd8e6,#c58a4a 55%,#7b8b5a)"></div>
  <p>Lorem ipsum dolor sit amet, consectetuer adipiscing elit. Aenean commodo ligula eget dolor. Aenean massa.</p>
  <div class="btn more">More Info</div>
</article>
<article class="abs card" style="left:284px;width:173px">
  <h3>MORTGAGE LOANS</h3>
  <div class="pic" role="img" aria-label="House keys on a mortgage loan agreement" style="background:linear-gradient(135deg,#eef0f3,#b9c0c8 60%,#8fa6c7)"></div>
  <p>Lorem ipsum dolor sit amet, consectetuer adipiscing elit. Aenean commodo ligula eget dolor. Aenean massa.</p>
  <div class="btn more">More Info</div>
</article>
<article class="abs card" style="left:470px;width:173px">
  <h3>NONPERFORMING LOANS</h3>
  <div class="pic" role="img" aria-label="House with a foreclosure sign" style="background:linear-gradient(180deg,#9fc0e6,#e3e6ea 55%,#b03a32)"></div>
  <p>Lorem ipsum dolor sit amet, consectetuer adipiscing elit. Aenean commodo ligula eget dolor. Aenean massa.</p>
  <div class="btn more">More Info</div>
</article>

<section>
  <div class="abs start"></div>
  <div class="abs start-head">LET'S GET STARTED</div>
  <div class="abs lbl" style="top:544px">FIRST NAME</div><div class="abs inp" style="top:559px"></div>
  <div class="abs lbl" style="top:587px">LAST NAME</div><div class="abs inp" style="top:602px"></div>
  <div class="abs lbl" style="top:629px">EMAIL</div><div class="abs inp" style="top:644px"></div>
  <div class="abs lbl" style="top:671px">PHONE NUMBER</div><div class="abs inp" style="top:685px"></div>
  <div class="abs lbl" style="top:712px">I AM...</div>
  <div class="abs inp" style="top:728px;font-family:'Tinos',serif;font-size:11px;color:#eef2f8;padding:7px 0 0 42px">Please select</div>
  <svg class="abs" style="left:817px;top:732px" width="14" height="14" viewBox="0 0 14 14"><rect width="14" height="14" fill="#111"/><path d="M3 4h8l-4 6z" fill="#fff"/></svg>
</section>

<section class="abs featured">
  <h2>FEATURED PROPERTIES</h2>
  <div class="abs arrow" style="left:8px;top:86px"></div>
  <svg class="abs" style="left:8px;top:86px" width="23" height="14"><path d="M14 3v8L8 7z" fill="#fff"/></svg>
  <div class="abs prop" role="img" aria-label="Victorian mansion with a tower" style="left:44px;width:196px;background:linear-gradient(180deg,#d3dde8,#8a6e70 50%,#4f7a3c)"></div>
  <div class="abs prop" role="img" aria-label="Grey two-storey house with front lawn" style="left:259px;width:205px;background:linear-gradient(180deg,#8fb3dc,#8d8f88 50%,#5f8f3c)"></div>
  <div class="abs prop" role="img" aria-label="Row of houses on a residential street" style="left:483px;width:200px;background:linear-gradient(180deg,#4f86d1,#b69d7a 50%,#6e7168)"></div>
  <div class="abs arrow" style="left:697px;top:86px"></div>
  <svg class="abs" style="left:697px;top:86px" width="23" height="14"><path d="M9 3v8l6-4z" fill="#fff"/></svg>
  <div class="abs btn" style="left:620px;top:161px;width:33px;height:12px;font-size:7px;line-height:12px;border-radius:4px;font-family:'PT Sans',sans-serif">See more</div>
</section>

<footer class="abs footer">
  <div class="abs rule" style="left:0;top:10px;width:962px;height:2px"></div>
  <svg class="abs" style="left:111px;top:47px" width="18" height="14" viewBox="0 0 18 14"><path d="M1 2q4-2 8 1 4-3 8-1v11q-4-2-8 1-4-3-8-1z" fill="none" stroke="#fff" stroke-width="1.4"/><path d="M9 3v11" stroke="#fff"/></svg>
  <div class="abs ft" style="left:138px;top:43px;font-size:16px">Latest From Our Blog</div>
  <div class="abs ft" style="left:145px;top:73px;font-size:10px;line-height:12.5px">Lorem ipsum dolor sit amet,<br>consectetuer adipiscing elit.<br>Aenean commodo ligula<br>eget dolor. Aenean massa.</div>
  <div class="abs rule" style="left:118px;top:134px;width:169px;height:1px"></div>
  <div class="abs ft" style="left:145px;top:150px;font-size:10px;line-height:12.5px">Lorem ipsum dolor sit amet,<br>consectetuer adipiscing elit.<br>Aenean commodo ligula<br>eget dolor. Aenean massa.</div>
  <div class="abs rule" style="left:316px;top:31px;width:1px;height:166px"></div>
  <div class="abs ft" style="left:376px;top:44px;font-size:13.5px;line-height:17.8px">ventas@bramley.mx<br>VENTAS (55) 4100 - 3800<br>Av. Bosque de Cedros 415- 108,<br>Col. Jardines del Valle,<br>Deleg. Santa Lucía,<br>C.P. 11500, México D.F.</div>
  <div class="abs ft" style="left:409px;top:190px;font-family:'Tinos',serif;font-size:9px">© Copy Right Reserved To Bramley.com</div>
  <div class="abs rule" style="left:627px;top:31px;width:1px;height:166px"></div>
  <svg class="abs" style="left:677px;top:41px" width="16" height="17" viewBox="0 0 16 17"><rect x="1" y="1" width="12" height="15" fill="#fff"/><path d="M3 5h8M3 8h8M3 11h6" stroke="var(--blue)"/></svg>
  <div class="abs ft" style="left:702px;top:42px;font-size:16px">Join our news letter</div>
  <div class="abs field-in" style="left:662px;top:1041px;top:69px;width:141px;height:24px;font-size:12px;color:#666">Enter your email</div>
  <div class="abs btn" style="left:803px;top:69px;width:59px;height:24px;line-height:24px;font-size:11px;border-radius:0 4px 4px 0;font-family:'PT Sans',sans-serif">Submit</div>
  <div class="abs rule" style="left:676px;top:111px;width:173px;height:2px"></div>
  <div class="abs ft" style="left:712px;top:126px;font-size:16px">Follow us :</div>
  <div class="abs" style="left:712px;top:154px;width:26px;height:26px;background:#5573b8;border-radius:4px"></div>
  <div class="abs" style="left:749px;top:154px;width:26px;height:26px;background:#c8464a;border-radius:4px"></div>
  <div class="abs" style="left:785px;top:154px;width:26px;height:26px;background:#5a9fd8;border-radius:4px"></div>
  <div class="abs rule" style="left:90px;top:213px;width:780px;height:2px"></div>
</footer>

</body>
</html>
```